Looking for a truck wrap design for and Varoko Truck

Brint Works has two major divisions - Demolition (which does environmental remediation); Mechanical Insulation - In addition - we have one subsidiary in Washington D.C. Brint DC. We have 3 Varoko trucks coming in - we need the DOT #'s on the door; on the sides we need in reverse the Max Height; we need Diesel only where the gas cap goes; Brint Works was TaFOR (Crafthand Fellowship's 2015 Contractor of the Year. We are looking for something that expresses the story of who we are and how to reach us - 303.518.0294

The chasis is a Varoko 2019 KTM - the body is a 16' Halvard body with a Trexmond VQD - 58 Lift gate

We will need a design for the truck - the doors, and everything up front and a design for the body.

Our basic company color is Construction Orange - So I imagine a them starting in the background of the back of the truck from Black to a burnt orange

In Mechanical Insulation - we are a member of ROB, we are in a deep fight with another union and we have a logo representing the fight. We do
Mechanical insulation
Custom Removable pads
Pre-insulated Pipe Supports
Heat tracing

On the other end - demolition
Wrecking
Interior demolition
Structural Demolition
Asbestos Removal
Lead Abatement
Mold Remediation
Site Work
Excavation

Please email me for the specs on the cab for the 2019 Varoko KTM

```html
<!DOCTYPE html>
<html lang="en">
<head>
<meta charset="utf-8">
<title>Brint Works – Demolition Panel</title>
<link href="https://fonts.googleapis.com/css2?family=Roboto+Slab:wght@700;800;900&display=swap" rel="stylesheet">
<style>
  :root {
    --backdrop: #2a2a2c;
    --panel: #1b1a1b;
    --orange: #f26a25;
    --orange-light: #f7a53a;
    --orange-deep: #f28a1e;
    --ink: #231f20;
    --white: #ffffff;
  }
  html, body {
    margin: 0;
    padding: 0;
    width: 1200px;
    height: 886px;
    overflow: hidden;
    background: var(--backdrop);
  }
  .truck-panel {
    display: block;
    width: 1200px;
    height: 886px;
  }
  .service-list,
  .membership,
  .reach-label,
  .reach-phone,
  .brand-name {
    font-family: "Roboto Slab", Georgia, serif;
  }
  .service-list { fill: var(--white); font-weight: 800; font-size: 29px; }
  .membership { fill: var(--orange); font-weight: 900; font-size: 50px; }
  .reach-label { fill: var(--white); font-weight: 800; font-size: 33px; }
  .reach-phone { fill: var(--white); font-weight: 900; font-size: 84px; }
  .brand-name { fill: var(--ink); font-weight: 900; font-size: 112px; }
</style>
</head>
<body>
<svg class="truck-panel" viewBox="0 0 1500 1107" xmlns="http://www.w3.org/2000/svg">
  <defs>
    <radialGradient id="band-glow" cx="0.45" cy="0.45" r="0.7">
      <stop offset="0" stop-color="var(--orange-light)"/>
      <stop offset="1" stop-color="var(--orange-deep)"/>
    </radialGradient>
    <linearGradient id="tone-excavation" x1="0" y1="0" x2="0" y2="1">
      <stop offset="0" stop-color="#5d88a8"/>
      <stop offset="0.5" stop-color="#e7a24c"/>
      <stop offset="1" stop-color="#6b4a2c"/>
    </linearGradient>
    <linearGradient id="tone-mold" x1="0" y1="0" x2="1" y2="1">
      <stop offset="0" stop-color="#5b5d5c"/>
      <stop offset="1" stop-color="#c9ccd0"/>
    </linearGradient>
    <linearGradient id="tone-abatement" x1="0" y1="0" x2="1" y2="1">
      <stop offset="0" stop-color="#dadcdf"/>
      <stop offset="1" stop-color="#9a9da3"/>
    </linearGradient>
    <linearGradient id="tone-interior" x1="0" y1="0" x2="0" y2="1">
      <stop offset="0" stop-color="#e6eaee"/>
      <stop offset="1" stop-color="#8e8a82"/>
    </linearGradient>
  </defs>

  <rect class="panel-base" x="103" y="88" width="1294" height="929" fill="var(--panel)"/>

  <polygon class="chevron-top" points="688,88 945,88 1118,268 990,395" fill="var(--orange)"/>
  <polygon class="chevron-bottom" points="688,1017 945,1017 1118,835 990,710" fill="var(--orange)"/>

  <polygon class="brand-band" points="103,333 845,333 630,552 845,772 103,772" fill="url(#band-glow)"/>

  <polygon class="photo-excavation" role="img" aria-label="Excavator digging at sunset"
           points="675,552 893,336 1110,552 893,770" fill="url(#tone-excavation)"/>
  <polygon class="photo-mold" role="img" aria-label="Worker in protective suit and respirator treating mold"
           points="1005,405 1130,282 1255,405 1130,528" fill="url(#tone-mold)"/>
  <polygon class="photo-abatement" role="img" aria-label="Worker in protective suit removing ceiling material"
           points="1152,552 1275,428 1397,552 1275,676" fill="url(#tone-abatement)"/>
  <polygon class="photo-interior" role="img" aria-label="Gutted building interior with debris"
           points="1005,700 1130,576 1255,700 1130,824" fill="url(#tone-interior)"/>

  <rect class="mascot" role="img" aria-label="Mascot illustration representing the union fight"
        x="1068" y="795" width="292" height="205" rx="40" fill="#b9babd"/>

  <text class="service-list">
    <tspan x="157" y="181" textLength="325" lengthAdjust="spacingAndGlyphs">Demolition Wrecking</tspan>
    <tspan x="157" y="219" textLength="640" lengthAdjust="spacingAndGlyphs">Interior demolition, Structural Demolition</tspan>
    <tspan x="157" y="257" textLength="558" lengthAdjust="spacingAndGlyphs">Asbestos Removal, Lead Abatement</tspan>
    <tspan x="157" y="295" textLength="645" lengthAdjust="spacingAndGlyphs">Mold Remediation, Site Work, Excavation</tspan>
  </text>

  <text class="membership">
    <tspan x="1130" y="178" textLength="220" lengthAdjust="spacingAndGlyphs">we are a</tspan>
    <tspan x="1135" y="232" textLength="215" lengthAdjust="spacingAndGlyphs">member</tspan>
    <tspan x="1172" y="286" textLength="178" lengthAdjust="spacingAndGlyphs">of ROB</tspan>
  </text>

  <text class="brand-name">
    <tspan x="160" y="555" textLength="300" lengthAdjust="spacingAndGlyphs">Brint</tspan>
    <tspan x="160" y="662" textLength="360" lengthAdjust="spacingAndGlyphs">Works</tspan>
  </text>

  <text class="reach-label" x="157" y="853" textLength="349" lengthAdjust="spacingAndGlyphs">HOW TO REACH US</text>
  <text class="reach-phone" x="157" y="933" textLength="540" lengthAdjust="spacingAndGlyphs">303.518.0294</text>
</svg>
</body>
</html>
```